Managed Service Provider need new business cards

We are a small Maanged Service Provider of IT Services and need a new fresh design for our business cards. We want something impossible, fun and professional :)
Our services has a large range, but we are always fun and make sure our customers both get their issue sorted and also feel like they are "catching up with an old friend".
All our cards in the past has always been all black, with red and we need something fresher.
The back of card, we would like just a small list of what we do i think, but if someone has a better idea, please do something cool with the back of the card:
Managed IT Services
Productivity Solutions
Data Backup and Recovery
IT System Maintenance
Managed IT Security
More details can be found on our website tqnetworks.com.au
Industry/Entity Type
It Company
Contact Information for Business Card
Name: Dwayne Falstrup
Title: Director
Phone: 03 6193 4827
Mobile: 0412 587 239
Email: dwayne@tqnetworks.com.au
Web: www.tqnetworks.com.au

```html
<!DOCTYPE html>
<html lang="en">
<head>
<meta charset="utf-8">
<title>TQ Networks — Business Cards</title>
<link href="https://fonts.googleapis.com/css2?family=Tenor+Sans&display=swap" rel="stylesheet">
<style>
  :root {
    --red: #e31b23;
    --red-deep: #b5121b;
    --ink: #4a4a4a;
    --ink-soft: #6b6b6b;
    --paper: #ffffff;
    --paper-shade: #f1f1f1;
    --backdrop: #e4e4e4;
    --rule: #9a9a9a;
  }
  * { box-sizing: border-box; margin: 0; padding: 0; }
  html, body { width: 1200px; height: 900px; overflow: hidden; }
  body {
    background: var(--backdrop);
    font-family: "Tenor Sans", "Helvetica Neue", Arial, sans-serif;
    color: var(--ink);
    position: relative;
  }
  .card {
    position: absolute;
    left: 250px;
    width: 700px;
    height: 400px;
    background: linear-gradient(135deg, var(--paper) 0%, var(--paper-shade) 100%);
    box-shadow: 0 6px 18px rgba(0,0,0,0.18);
    overflow: hidden;
  }
  .card--back { top: 30px; }
  .card--front { top: 470px; }
  .card__swoosh { position: absolute; inset: 0; width: 700px; height: 400px; }

  .brand {
    position: absolute;
    display: flex;
    align-items: center;
    gap: 12px;
    color: var(--red);
    font-size: 40px;
    letter-spacing: 2px;
    white-space: nowrap;
  }
  .brand__dot {
    width: 26px; height: 26px;
    border: 3px solid var(--red);
    border-radius: 50%;
  }
  .card--back .brand { left: 190px; top: 55px; }
  .card--front .brand { left: 50px; top: 80px; }

  .services {
    position: absolute;
    left: 0; right: 0;
    top: 145px;
    text-align: center;
  }
  .services__title {
    font-size: 20px;
    letter-spacing: 1px;
    color: var(--ink);
    margin-bottom: 10px;
  }
  .services__line {
    font-size: 19px;
    color: var(--ink-soft);
    line-height: 1.65;
  }
  .services__star { color: var(--red); margin: 0 8px; font-size: 16px; }

  .person {
    position: absolute;
    right: 330px;
    top: 240px;
    text-align: right;
  }
  .person__name { color: var(--red); font-size: 22px; letter-spacing: 1px; text-transform: uppercase; }
  .person__title { color: var(--ink-soft); font-size: 18px; margin-top: 2px; }

  .contact {
    position: absolute;
    left: 395px;
    top: 140px;
    padding-left: 22px;
    border-left: 1px solid var(--rule);
    list-style: none;
  }
  .contact__item {
    display: flex;
    align-items: center;
    gap: 10px;
    font-size: 16px;
    color: var(--ink);
    line-height: 1.75;
    white-space: nowrap;
  }
  .contact__icon { width: 14px; height: 14px; fill: var(--red); flex: none; }
</style>
</head>
<body>

  <section class="card card--back" aria-label="Card back">
    <svg class="card__swoosh" viewBox="0 0 700 400" aria-hidden="true">
      <path d="M0 400 L0 372 C300 372 520 332 700 250 L700 400 Z" fill="var(--red)"/>
      <path d="M0 378 C300 378 520 340 700 262 L700 256 C520 334 300 374 0 374 Z" fill="var(--paper)"/>
      <path d="M0 388 C220 386 420 362 580 318 C430 352 220 376 0 380 Z" fill="var(--red-deep)"/>
    </svg>
    <div class="brand"><span class="brand__dot"></span>TQ NETWORKS</div>
    <div class="services">
      <h2 class="services__title">SERVICES</h2>
      <p class="services__line">Managed IT Services<span class="services__star">✦</span>Productivity Solutions</p>
      <p class="services__line">Data Backup and Recovery<span class="services__star">✦</span>IT System Maintenance</p>
      <p class="services__line">Managed IT Security</p>
    </div>
  </section>

  <section class="card card--front" aria-label="Card front">
    <svg class="card__swoosh" viewBox="0 0 700 400" aria-hidden="true">
      <path d="M0 400 L0 350 C300 354 520 334 700 292 L700 400 Z" fill="var(--red)"/>
      <path d="M0 356 C300 360 520 342 700 304 L700 298 C520 336 300 356 0 352 Z" fill="var(--paper)"/>
      <path d="M420 340 C540 330 630 312 700 292 L700 286 C630 306 540 324 420 340 Z" fill="var(--paper)"/>
      <path d="M420 328 C540 318 630 298 700 276 L700 270 C630 292 540 312 420 328 Z" fill="var(--red-deep)"/>
    </svg>
    <div class="brand"><span class="brand__dot"></span>TQ NETWORKS</div>
    <div class="person">
      <p class="person__name">Dwayne Falstrup</p>
      <p class="person__title">Director</p>
    </div>
    <ul class="contact">
      <li class="contact__item">
        <svg class="contact__icon" viewBox="0 0 14 14" aria-hidden="true"><path d="M4 0h6a1 1 0 0 1 1 1v12a1 1 0 0 1-1 1H4a1 1 0 0 1-1-1V1a1 1 0 0 1 1-1zm0.5 1.5v10h5v-10z"/></svg>
        0412 587 239
      </li>
      <li class="contact__item">
        <svg class="contact__icon" viewBox="0 0 14 14" aria-hidden="true"><path d="M1 4c0-2 2-3 6-3s6 1 6 3v1h-3V4H4v1H1zM3 6h8l2 7H1z"/></svg>
        03 6193 4827
      </li>
      <li class="contact__item">
        <svg class="contact__icon" viewBox="0 0 14 14" aria-hidden="true"><path d="M0 3h14v9H0zM1 4l6 4 6-4v-0.2H1z"/></svg>
        dwayne@tqnetworks.com.au
      </li>
      <li class="contact__item">
        <svg class="contact__icon" viewBox="0 0 14 14" aria-hidden="true"><circle cx="7" cy="7" r="7"/><path d="M1 7h12M7 1c-3 3-3 9 0 12M7 1c3 3 3 9 0 12" stroke="#fff" stroke-width="0.9" fill="none"/></svg>
        www.tqnetworks.com.au
      </li>
    </ul>
  </section>

</body>
</html>
```